Business cards for 3 Realtors at one brokerage

We will need a business card template that can be projected on 3 business cards. Summit Crest Property & Holdings Corp. has 3 realtors on staff Dale, Owen, and Brady. We all want a business card that shows our new logo and information. I will attach many versions of our Logo as well as head shots for each realtor (Owen- Long hair, youngest. Brady- Suit jacket, parted hair cut. Dale- Angled Pose, Shirt and Tie.) I have attached our information below.

Dale Forsythe
801-555-0147
dale@summitcresthomes.com
Principal Broker

Brady Tidwell
801-555-0192
brady@summitcresthomes.com
Real Estate Agent

Owen Tidwell
801-555-0163
owen@summitcresthomes.com
Real Estate Agent

Summit Crest Property & Holdings Corp.
SummitCrestHomes.com
2918 W 8650 Suite 204-117, South Jordan, UT 84009

Please feel free to reach out with any questions, comments, or concerns.

```html
<!DOCTYPE html>
<html lang="en">
<head>
<meta charset="utf-8">
<title>Summit Crest Property &amp; Holdings Corp. – Business Cards</title>
<link rel="stylesheet" href="https://fonts.googleapis.com/css2?family=Montserrat:wght@400;500;600&display=swap">
<style>
  :root {
    --backdrop: #bdbdbd;
    --brand-blue: #4fa3db;
    --brand-gray: #6f6f6e;
    --ink: #4a4a4a;
    --white: #ffffff;
  }
  * { box-sizing: border-box; margin: 0; padding: 0; }
  html, body { width: 1200px; height: 1188px; overflow: hidden; }
  body {
    background: var(--backdrop);
    font-family: "Montserrat", Arial, sans-serif;
    position: relative;
  }
  .card {
    position: absolute;
    width: 477px;
    height: 272px;
    border-radius: 17px;
    overflow: hidden;
    box-shadow: 0 14px 18px rgba(0,0,0,0.22);
    background: var(--white);
  }
  .col-front { left: 86px; }
  .col-back { left: 637px; }
  .row-1 { top: 120px; }
  .row-2 { top: 458px; }
  .row-3 { top: 796px; }

  /* front */
  .brand {
    position: absolute; left: 23px; top: 23px;
    display: flex; align-items: center; gap: 9px;
    color: var(--brand-gray); font-weight: 500;
    z-index: 2;
  }
  .brand-dot {
    width: 55px; height: 55px; border-radius: 50%;
    border: 3px solid var(--brand-blue);
  }
  .brand-name { line-height: 1; }
  .brand-name .main { display: block; font-size: 19px; letter-spacing: 0.5px; }
  .brand-name .sub { display: block; font-size: 7px; letter-spacing: 1.8px; margin-top: 4px; padding-left: 2px; }

  .tab {
    position: absolute; left: -4px; top: 103px;
    width: 12px; height: 29px; border-radius: 6px;
    background: var(--brand-blue);
  }
  .agent { position: absolute; left: 22px; top: 96px; color: var(--ink); z-index: 2; }
  .agent-name { font-size: 18px; font-weight: 600; color: var(--brand-blue); line-height: 1.1; }
  .agent-title { font-size: 12.5px; margin-top: 2px; }
  .address { font-size: 12.5px; line-height: 17.5px; margin-top: 14px; }
  .contact { list-style: none; font-size: 12.5px; line-height: 17.5px; margin-top: 14px; }
  .contact li { display: flex; align-items: center; gap: 5px; }
  .contact svg { width: 10px; height: 10px; fill: var(--brand-blue); }

  .headshot {
    position: absolute; right: 20px; top: 14px;
    width: 180px; height: 240px;
    border-radius: 90px 90px 0 0;
  }
  .headshot.dale { background: linear-gradient(180deg, #8a5a3a 0%, #e0b8a0 35%, #f2f2f2 70%, #ffffff 100%); }
  .headshot.brady { background: linear-gradient(180deg, #5a4030 0%, #e3b89c 38%, #7f86c4 72%, #8a90cc 100%); }
  .headshot.owen { background: linear-gradient(180deg, #6a6460 0%, #d9ab90 38%, #9a9a98 70%, #8d8d8b 100%); }

  .swoosh { position: absolute; left: 0; bottom: 0; width: 477px; height: 272px; }
  .website {
    position: absolute; right: 18px; bottom: 12px;
    color: var(--white); font-size: 12.5px; font-weight: 500; letter-spacing: 0.2px;
  }

  /* back */
  .back-mark {
    position: absolute; left: 0; right: 0; top: 60px;
    display: flex; flex-direction: column; align-items: center;
    font-weight: 500;
  }
  .back-dot { width: 98px; height: 98px; border-radius: 50%; border: 5px solid var(--brand-blue); }
  .back-name { text-align: center; line-height: 1; margin-top: 14px; }
  .back-name .main { display: block; font-size: 29px; letter-spacing: 0.6px; }
  .back-name .sub { display: block; font-size: 11px; letter-spacing: 3.5px; margin-top: 8px; }
  .back-white .back-name { color: var(--brand-gray); }
  .back-gray { background: var(--brand-gray); }
  .back-gray .back-name { color: var(--white); }
  .back-blue { background: var(--brand-blue); }
  .back-blue .back-name { color: var(--white); }
  .back-blue .back-dot { border-color: var(--white); }
</style>
</head>
<body>

<svg width="0" height="0" style="position:absolute">
  <defs>
    <symbol id="icon-phone" viewBox="0 0 24 24"><path d="M6.6 10.8a15.1 15.1 0 0 0 6.6 6.6l2.2-2.2a1 1 0 0 1 1-.25 11.4 11.4 0 0 0 3.6.57 1 1 0 0 1 1 1V20a1 1 0 0 1-1 1A17 17 0 0 1 3 4a1 1 0 0 1 1-1h3.5a1 1 0 0 1 1 1c0 1.25.2 2.45.57 3.6a1 1 0 0 1-.25 1z"/></symbol>
    <symbol id="icon-mail" viewBox="0 0 24 24"><path d="M2 5h20v2l-10 6L2 7z M2 9l10 6 10-6v10H2z"/></symbol>
  </defs>
</svg>

<!-- Dale -->
<article class="card col-front row-1">
  <div class="headshot dale" role="img" aria-label="Headshot of Dale Forsythe"></div>
  <div class="brand"><span class="brand-dot"></span><span class="brand-name"><span class="main">SUMMIT CREST</span><span class="sub">PROPERTY &amp; HOLDINGS CORP.</span></span></div>
  <span class="tab"></span>
  <div class="agent">
    <h2 class="agent-name">Dale Forsythe</h2>
    <p class="agent-title">Principal Broker</p>
    <p class="address">2918 W 8650 Suite 204-117<br>Aspen Fork, ST 00000</p>
    <ul class="contact">
      <li><svg><use href="#icon-phone"/></svg>801-555-0147</li>
      <li><svg><use href="#icon-mail"/></svg>dale@summitcresthomes.com</li>
    </ul>
  </div>
  <svg class="swoosh" viewBox="0 0 477 272">
    <path fill="var(--brand-gray)" d="M95,258 C200,255 280,225 360,213 C410,206 450,207 477,211 L477,224 C440,217 400,216 350,225 C270,240 190,258 95,258 Z"/>
    <path fill="var(--brand-blue)" d="M0,242 C110,268 250,262 330,240 C390,224 440,224 477,233 L477,272 L0,272 Z"/>
  </svg>
  <span class="website">SummitCrestHomes.com</span>
</article>

<!-- Brady -->
<article class="card col-front row-2">
  <div class="headshot brady" role="img" aria-label="Headshot of Brady Tidwell"></div>
  <div class="brand"><span class="brand-dot"></span><span class="brand-name"><span class="main">SUMMIT CREST</span><span class="sub">PROPERTY &amp; HOLDINGS CORP.</span></span></div>
  <span class="tab"></span>
  <div class="agent">
    <h2 class="agent-name">Brady Tidwell</h2>
    <p class="agent-title">Real Estate Agent</p>
    <p class="address">2918 W 8650 Suite 204-117<br>Aspen Fork, ST 00000</p>
    <ul class="contact">
      <li><svg><use href="#icon-phone"/></svg>801-555-0192</li>
      <li><svg><use href="#icon-mail"/></svg>brady@summitcresthomes.com</li>
    </ul>
  </div>
  <svg class="swoosh" viewBox="0 0 477 272">
    <path fill="var(--brand-blue)" d="M95,258 C200,255 280,225 360,213 C410,206 450,207 477,211 L477,224 C440,217 400,216 350,225 C270,240 190,258 95,258 Z"/>
    <path fill="var(--brand-gray)" d="M0,242 C110,268 250,262 330,240 C390,224 440,224 477,233 L477,272 L0,272 Z"/>
  </svg>
  <span class="website">SummitCrestHomes.com</span>
</article>

<!-- Owen -->
<article class="card col-front row-3">
  <div class="headshot owen" role="img" aria-label="Headshot of Owen Tidwell"></div>
  <div class="brand"><span class="brand-dot"></span><span class="brand-name"><span class="main">SUMMIT CREST</span><span class="sub">PROPERTY &amp; HOLDINGS CORP.</span></span></div>
  <span class="tab"></span>
  <div class="agent">
    <h2 class="agent-name">Owen Tidwell</h2>
    <p class="agent-title">Real Estate Agent</p>
    <p class="address">2918 W 8650 Suite 204-117<br>Aspen Fork, ST 00000</p>
    <ul class="contact">
      <li><svg><use href="#icon-phone"/></svg>801-555-0163</li>
      <li><svg><use href="#icon-mail"/></svg>owen@summitcresthomes.com</li>
    </ul>
  </div>
  <svg class="swoosh" viewBox="0 0 477 272">
    <path fill="var(--brand-gray)" d="M95,258 C200,255 280,225 360,213 C410,206 450,207 477,211 L477,224 C440,217 400,216 350,225 C270,240 190,258 95,258 Z"/>
    <path fill="var(--brand-blue)" d="M0,242 C110,268 250,262 330,240 C390,224 440,224 477,233 L477,272 L0,272 Z"/>
  </svg>
  <span class="website">SummitCrestHomes.com</span>
</article>

<!-- Backs -->
<article class="card col-back row-1 back-white">
  <div class="back-mark"><span class="back-dot"></span><span class="back-name"><span class="main">SUMMIT CREST</span><span class="sub">PROPERTY &amp; HOLDINGS CORP.</span></span></div>
</article>
<article class="card col-back row-2 back-gray">
  <div class="back-mark"><span class="back-dot"></span><span class="back-name"><span class="main">SUMMIT CREST</span><span class="sub">PROPERTY &amp; HOLDINGS CORP.</span></span></div>
</article>
<article class="card col-back row-3 back-blue">
  <div class="back-mark"><span class="back-dot"></span><span class="back-name"><span class="main">SUMMIT CREST</span><span class="sub">PROPERTY &amp; HOLDINGS CORP.</span></span></div>
</article>

</body>
</html>
```